Harlow Crest Holdings (Remodeling company) needs a logo and business card

We need a business card design for a new company. We "flip" upmarket houses (buy, remodel and sell) in the Austin, TX area. I'd like neutral colors (grey, white, gold black). I would like it to include a simple, clean logo. Our designs are modern and uncluttered and I would like that reflected in the business card design.

Target Market(s)

Young professionals, Families, Retirees. Our properties will sell for $750k+

Industry/Entity Type

Real Estate

Contact Information for Business Card

Harlow Crets Holdings
Mona Harlow
(979) 555 0142
Owner
Rolf Tandem
(512) 555 0176
Realtor

Logo Text

Harlow Crest Holdings

Font styles to use
Serif
Script

Requirements
Must have
• Simple, classic design
Nice to have
• Clean lines, modern look
Should not have
• Too traditionally

```html
<!DOCTYPE html>
<html lang="en">
<head>
<meta charset="utf-8">
<title>Harlow Crest Holdings – Business Card</title>
<link href="https://fonts.googleapis.com/css2?family=Open+Sans:wght@400;600;700&display=swap" rel="stylesheet">
<style>
  :root {
    --backdrop: #d9d9d9;
    --card-black: #000000;
    --card-grey: #a3a3a3;
    --band-white: #e6e6e6;
    --band-dark: #222222;
    --text-silver: #c9c9c9;
    --text-light: #ececec;
    --text-dark: #1a1a1a;
  }
  * { box-sizing: border-box; margin: 0; padding: 0; }
  html, body {
    width: 1200px;
    height: 900px;
    overflow: hidden;
    background: var(--backdrop);
    font-family: "Open Sans", Arial, sans-serif;
  }
  .canvas {
    position: relative;
    width: 1200px;
    height: 900px;
  }
  .card {
    position: absolute;
    width: 560px;
    height: 320px;
    left: 320px;
    overflow: hidden;
    box-shadow: 0 6px 18px rgba(0,0,0,0.25);
  }
  .card-front {
    top: 70px;
    background: var(--card-black);
    display: flex;
    flex-direction: column;
    align-items: center;
    justify-content: center;
    gap: 22px;
  }
  .brand-dot {
    width: 34px;
    height: 34px;
    border-radius: 50%;
    background: var(--text-silver);
  }
  .brand-name {
    color: var(--text-silver);
    font-weight: 400;
    font-size: 36px;
    letter-spacing: 1px;
  }
  .card-back {
    top: 470px;
    background: var(--card-grey);
  }
  .back-shape {
    position: absolute;
    left: 0;
    top: 0;
  }
  .back-brand {
    position: absolute;
    left: 24px;
    top: 142px;
    width: 230px;
    text-align: center;
    color: var(--text-light);
    font-weight: 400;
    font-size: 22px;
    line-height: 1.25;
  }
  .contacts {
    position: absolute;
    right: 40px;
    top: 52px;
    text-align: right;
  }
  .contact + .contact { margin-top: 34px; }
  .contact-name {
    font-weight: 700;
    font-size: 21px;
    line-height: 1.3;
    color: var(--text-light);
  }
  .contact-role {
    font-size: 15px;
    line-height: 1.4;
    color: var(--text-dark);
  }
  .contact-phone {
    font-size: 15px;
    line-height: 1.4;
    color: var(--text-dark);
    display: flex;
    align-items: center;
    justify-content: flex-end;
    gap: 7px;
  }
  .phone-icon {
    display: block;
    width: 14px;
    height: 14px;
    flex: none;
  }
</style>
</head>
<body>
<main class="canvas">
  <section class="card card-front">
    <div class="brand-dot"></div>
    <div class="brand-name">Harlow Crets Holdings</div>
  </section>

  <section class="card card-back">
    <svg class="back-shape" viewBox="0 0 560 320" width="560" height="320" aria-hidden="true">
      <path d="M0 0 H300 C360 80 350 240 220 320 H0 Z" fill="var(--band-white)"/>
      <path d="M0 0 H285 C340 85 330 235 200 320 H0 Z" fill="var(--card-black)"/>
      <path d="M296 0 C350 80 345 235 228 320 H222 C335 235 342 85 291 0 Z" fill="var(--band-dark)"/>
    </svg>
    <div class="back-brand">Harlow Crets<br>Holdings</div>
    <div class="contacts">
      <div class="contact">
        <div class="contact-name">Rolf Tandem</div>
        <div class="contact-role">Realtor</div>
        <div class="contact-phone">
          <span>(512) 555 0176</span>
          <svg class="phone-icon" viewBox="0 0 14 14" aria-hidden="true"><path d="M1 5 Q7 0 13 5 L11 7 L9 5 H5 L3 7 Z M3 8 H11 V12 H3 Z" fill="var(--text-dark)"/></svg>
        </div>
      </div>
      <div class="contact">
        <div class="contact-name">Mona Harlow</div>
        <div class="contact-role">Owner</div>
        <div class="contact-phone">
          <span>(979) 555 0142</span>
          <svg class="phone-icon" viewBox="0 0 14 14" aria-hidden="true"><path d="M1 5 Q7 0 13 5 L11 7 L9 5 H5 L3 7 Z M3 8 H11 V12 H3 Z" fill="var(--text-dark)"/></svg>
        </div>
      </div>
    </div>
  </section>
</main>
</body>
</html>
```